Banner ad design for Vantora Display Ads

We are looking for a designer to develop a concept for banner ads for a Vantora Display campaign we are building.

We have 3 business lines, shredding services, records management services and scanning services.

We are looking for 4 sets of ads to be created, one for each business line + one set that showcases all of our lines together.

For the design concepts, we would like to see a few sizes (banner, square, leaderboard, skyscraper, etc) for each.

The person chosen will then need to create the ads into all Vantora supported sizes -- 20 sizes total for each set of ads as per the Vantora size guidelines found on this page - https://help.vantora-example.com/vantora-ads/answer/4827150?hl=en&ref_topic=6604821#

A few items to note:
- Design should complement our existing brand/website look and feel (www.oak-ferry.ca)
- Each final ad must be 150Kb or less in size
- Final designs should be editable, meaning if we would like to change some copy in the design, we can do so using a well-known software (Canva, Photoshop/InDesign, etc)
- Some images are attached for use, but if you feel a different stock image is more suitable to to your design, please go ahead and use it.

Provided below is some messaging that can be used for each set of ads. Do not feel you need to use all of the messaging, it is provided for guidance.

SHREDDING SERVICES:

Possible Short Headline:
-- One-Time Shredding Services
-- Secure Shredding Services
-- Affordable On-Site Shredding

Possible Long Headline
-- Your Paper Can be Destroyed as Soon as the Next Business Day

Possible Descriptions:
-- KVEC Gold Certified On site shredding company. Service as soon as Next Day.
-- Secure and Affordable Toronto & GTA On-Site Shredding.
-- Certified, Affordable Office Shredding Since 2003.
-- Quick, no contact and affordable paper shredding services in Toronto & Southern Ontario.
-- Certified, Affordable Office Shredding Since 2003. Fast, no contact shredding service.

Call to Action
-- Get a Quote

RECORDS MANAGEMENT
Short Headline:
-- Off-site Records Storage
-- Records Management & Storage
-- Secure Records Storage
-- Records Management Services
-- Long Term Records Management
-- Document Storage Solutions

Possible Description
-- Local, Affordable Storage Solutions. Protect and Store your Documents in our Secure Facility
-- Local, Affordable Records Management Solutions. Store your Records in our Secure Facility
-- Certified, Affordable Document Storage Since 2004. Contact Us for a Free Quote!
-- Vaultline+ Certified, Affordable Document Storage Since 2004. Contact Us for a Free Quote!

Call to Action
-- Get a Quote

SCANNING SERVICES

Short Headline:
-- Professional Scanning Company
-- Toronto & GTA Scanning Service
-- Document Scanning Services
-- Digital Conversion Services
-- Fast & Easy Retrieval

Description
-- Scan and documents and files with Professional scanning services from Oak-Ferry
-- Convert Your Paper Files to Electronic Files. Fast & Easy Retrieval.
-- Easily access your documents electronically with Document Scanning Services

Call to Action
-- Get a Quote

ALL SERVICES AD SET
Short Headline
-- Shred, Scan & Store Documents
-- Secure Shredding, Records Management and Scanning Services
-- #1 Document Management Company
-- Oak Ferry Shredding, Storage & Scanning

Description
-- Secure and Affordable Toronto & GTA On-Site Shredding, Document Storage & Scanning Company

Call to Action
-- Get a Quote

Font styles to use
Sans Serif

```html
<!DOCTYPE html>
<html lang="en">
<head>
<meta charset="utf-8">
<title>Oak-Ferry Display Banners</title>
<link rel="stylesheet" href="https://fonts.googleapis.com/css2?family=Poppins:wght@600;700&family=Open+Sans:wght@400;600;700&display=swap">
<style>
  :root {
    --brand-blue: #1b8ae0;
    --ink-dark: #232323;
    --ink-navy: #1f2a44;
    --paper-grey: #f0efed;
    --white: #ffffff;
    --night: #2b2b2b;
  }
  * { box-sizing: border-box; margin: 0; padding: 0; }
  html, body { width: 1200px; height: 1200px; overflow: hidden; background: var(--white); }
  body { position: relative; font-family: "Open Sans", Arial, sans-serif; }

  .banner { position: absolute; left: 43px; width: 1116px; height: 216px; overflow: hidden; }
  .banner--scanning { top: 53px; background: var(--brand-blue); }
  .banner--storage { top: 323px; background: var(--night); }
  .banner--shredding { top: 602px; background: var(--paper-grey); }
  .banner--all { top: 898px; background: var(--brand-blue); }

  .photo { position: absolute; top: 0; height: 100%; }

  .headline {
    position: absolute;
    font-family: "Poppins", Arial, sans-serif;
    font-weight: 700;
    font-size: 26px;
    line-height: 1.2;
    text-transform: uppercase;
    color: var(--white);
    white-space: nowrap;
  }
  .body-copy {
    position: absolute;
    font-size: 20px;
    line-height: 28px;
    color: var(--white);
  }
  .cta {
    position: absolute;
    width: 168px; height: 49px;
    display: flex; align-items: center; justify-content: center;
    font-family: "Poppins", Arial, sans-serif;
    font-weight: 600;
    font-size: 19px;
    color: var(--white);
  }
  .cta--dark { background: var(--ink-dark); }
  .cta--blue { background: var(--brand-blue); }

  .wordmark { position: absolute; display: flex; flex-direction: column; color: var(--white); }
  .wordmark__name {
    display: flex; align-items: center; gap: 6px;
    font-family: "Open Sans", Arial, sans-serif;
    font-weight: 700; font-size: 27px; line-height: 1;
  }
  .wordmark__mark { width: 12px; height: 12px; background: currentColor; }
  .wordmark__tag { font-size: 14px; line-height: 1; margin-top: 6px; letter-spacing: 0.3px; font-weight: 400; }
  .wordmark--navy { color: var(--ink-navy); }

  /* Scanning */
  .banner--scanning .photo {
    left: 600px; width: 516px;
    background: linear-gradient(120deg, #d8d8d8 0%, #f1f1f1 45%, #bdbdbd 75%, #3a3a3a 100%);
  }
  .banner--scanning .headline { left: 31px; top: 22px; }
  .banner--scanning .body-copy { left: 31px; top: 67px; }
  .banner--scanning .cta { left: 36px; top: 145px; }
  .banner--scanning .wordmark { left: 424px; top: 152px; }

  /* Storage */
  .banner--storage .photo {
    left: 0; width: 100%;
    background: linear-gradient(100deg, #1f1f1f 0%, #2e2e2e 40%, #4a4a4a 70%, #303030 100%);
  }
  .banner--storage .headline { left: 26px; top: 24px; }
  .banner--storage .body-copy { left: 29px; top: 69px; }
  .banner--storage .cta { left: 31px; top: 144px; }
  .banner--storage .wordmark { left: 888px; top: 125px; }

  /* Shredding */
  .banner--shredding .wordmark { left: 29px; top: 56px; }
  .shred-title {
    position: absolute; left: 226px; top: 22px;
    font-family: "Poppins", Arial, sans-serif; font-weight: 700;
    font-size: 25px; color: var(--brand-blue); white-space: nowrap;
  }
  .shred-lead {
    position: absolute; left: 229px; top: 63px;
    font-weight: 700; font-size: 21px; line-height: 29px; color: var(--ink-dark);
  }
  .shred-desc {
    position: absolute; left: 229px; top: 134px;
    font-size: 19px; line-height: 29px; color: var(--ink-dark);
  }
  .banner--shredding .cta { left: 28px; top: 127px; width: 168px; height: 50px; }
  .shred-stripe {
    position: absolute; top: 0; left: 654px; width: 462px; height: 100%;
    background: var(--brand-blue);
    clip-path: polygon(0 0, 100% 0, 100% 100%, 33px 100%);
  }
  .banner--shredding .photo {
    left: 663px; width: 453px;
    background: linear-gradient(110deg, #e9e7e4 0%, #d9d6d1 50%, #c9c5bf 100%);
    clip-path: polygon(0 0, 100% 0, 100% 100%, 33px 100%);
  }

  /* All services */
  .banner--all .photo {
    left: 0; width: 560px;
    background: linear-gradient(90deg, #c9c2b8 0%, #a9b1b8 45%, #5e8fbd 75%, rgba(27,138,224,0) 100%);
  }
  .banner--all .headline { left: 467px; top: 23px; }
  .banner--all .body-copy { left: 467px; top: 65px; }
  .banner--all .cta { left: 469px; top: 140px; }
  .banner--all .wordmark { left: 936px; top: 152px; }
</style>
</head>
<body>

<section class="banner banner--scanning">
  <div class="photo" role="img" aria-label="Hands placing paper documents into an office scanner"></div>
  <h2 class="headline">Professional Scanning Company</h2>
  <p class="body-copy">Scan and documents and files with Professional<br>scanning services from Oak-Ferry</p>
  <div class="cta cta--dark">Get a Quote</div>
  <div class="wordmark">
    <span class="wordmark__name">oak-ferry.<span class="wordmark__mark"></span></span>
    <span class="wordmark__tag">Information Security</span>
  </div>
</section>

<section class="banner banner--storage">
  <div class="photo" role="img" aria-label="Dimmed close-up of a hand leafing through stacked paper files"></div>
  <h2 class="headline">Off-Site Records Storage</h2>
  <p class="body-copy">Local, Affordable Storage Solutions. Protect and<br>Store your Documents in our Secure Facility.</p>
  <div class="cta cta--blue">Get a Quote</div>
  <div class="wordmark">
    <span class="wordmark__name">oak-ferry.<span class="wordmark__mark"></span></span>
    <span class="wordmark__tag">Information Security</span>
  </div>
</section>

<section class="banner banner--shredding">
  <div class="wordmark wordmark--navy">
    <span class="wordmark__name">oak-ferry.<span class="wordmark__mark"></span></span>
    <span class="wordmark__tag">Information Security</span>
  </div>
  <h2 class="shred-title">One-Time Shredding Services</h2>
  <p class="shred-lead">Your Paper Can be Destroyed as Soon<br>as the Next Business Day</p>
  <p class="shred-desc">Secure and Affordable Toronto &amp;<br>GTA On-Site Shredding.</p>
  <div class="cta cta--blue">Get a Quote</div>
  <div class="shred-stripe"></div>
  <div class="photo" role="img" aria-label="Hand sliding paper into a secure shredding console"></div>
</section>

<section class="banner banner--all">
  <div class="photo" role="img" aria-label="Uniformed service technician receiving a box of documents in an office"></div>
  <h2 class="headline">Shred, Scan &amp; Store Documents</h2>
  <p class="body-copy">Quick, no contact and affordable paper shredding<br>services in Toronto &amp; Southern Ontario.</p>
  <div class="cta cta--dark">Get a Quote</div>
  <div class="wordmark">
    <span class="wordmark__name">oak-ferry.<span class="wordmark__mark"></span></span>
    <span class="wordmark__tag">Information Security</span>
  </div>
</section>

</body>
</html>
```